Lumen Keyvault Password Manager WebApp Design

Lumen Keyvault is seeking an expert UI designer to provide a fresh and modern visual appeal for our product. Our inspiration comes from two major tools that have successfully managed to balance functionality and design aesthetics - Orbix Folder and Vaultmint. We want our application to exude a similar trustworthiness and modernity, through a clean, intuitive and responsive design.
We have established preliminary mockups and would like the designer to work within these parameters while enhancing the overall user experience. The primary tasks will involve innovative and improved designs of the login screen and the password screen, both being crucial touchpoints for our users. The login screen also serves a crucial role in demonstrating how our system works.
Key Elements:
Logo Integration: We are providing the logo for Lumen Keyvault. The design should align with the logo, both in terms of colors and overall aesthetic, to ensure a cohesive brand identity.
Color Palette: The UI design should adhere to the color palette derived from the logo to maintain brand consistency. The design should effectively utilize these colors to highlight important elements and improve user engagement.
Trustworthy and Modern Design: The UI should be professional and trustworthy. It should mirror the look and feel of Orbix Folder's simplicity and Vaultmint's solid security design, which inspires user confidence.
Adherence to Mockup Boundaries: The existing mockups serve as a guideline for the layout and placement of elements. The design should respect these boundaries while bringing innovation and visual appeal.
Improved Login Screen: The login screen is a key part of the user's journey and should be designed with utmost care. It should be intuitive, easy-to-use, visually engaging, and educative, showcasing how the system operates and encouraging users to sign in with confidence.
Enhanced Password Screen: The password screen, another key user touchpoint, needs improvement. The different types of passwords should be made more visible and intuitive, easing user interaction and enhancing the overall experience.
Prospective designers are encouraged to test our current version available for free at app.lumenkeyvault.com to understand the product better and contribute to meaningful design enhancements.
The goal of this project is to provide a visually compelling and user-friendly interface for Lumen Keyvault that inspires user trust, while adhering to the branding elements, including color scheme and logo design. The ideal designer will have a proven track record of creating compelling UI designs that enhance user experience and engagement.
We preferred the design to be in Figma.
Please provide the 3 design so we can evaluate if we like to choice you:
1. Login Page.
2. Passwords View design
3. Single Passwod Page
We need all the pages to be design that are provided as screenshots.

```html
<!DOCTYPE html>
<html lang="en">
<head>
<meta charset="utf-8">
<title>Lumen Keyvault – Login and Vault</title>
<link href="https://fonts.googleapis.com/css2?family=Manrope:wght@400;500;600;700;800&display=swap" rel="stylesheet">
<style>
:root{
  --stage:#283238;
  --white:#ffffff;
  --app-bg:#f5f7fa;
  --blue:#2f8af0;
  --blue-text:#2f8fe6;
  --blue-soft:#5aa7ef;
  --blue-pale:#e4edfc;
  --green:#1fa35c;
  --green-bright:#1dbf63;
  --green-text:#1c8c4c;
  --red:#e9523e;
  --red-soft:#e85a4f;
  --yellow:#f8c93a;
  --cyan:#2ec4ee;
  --cyan-pale:#eef7fc;
  --ink:#1f2328;
  --muted:#6b7280;
  --placeholder:#8fc0f0;
  --line:#e6ebf1;
}
*{box-sizing:border-box;margin:0;padding:0}
html,body{width:1200px;height:1200px;overflow:hidden;background:var(--stage)}
body{font-family:'Manrope',sans-serif;color:var(--ink)}
.board{position:absolute;left:0;top:0;width:1900px;height:1900px;transform:scale(0.63158);transform-origin:0 0}
.screen{position:absolute;left:266px;width:1366px;height:768px;overflow:hidden}
.screen--login{top:110px;background:var(--white)}
.screen--vault{top:1021px;background:var(--app-bg)}
.abs{position:absolute}
.brand{display:flex;align-items:center;gap:22px;color:var(--blue-text);font-weight:500}
.brand-mark{width:40px;height:40px;border-radius:6px;background:var(--blue)}
/* login */
.glow{left:300px;top:120px;width:760px;height:660px;border-radius:50%;
  background:radial-gradient(circle at 30% 45%,rgba(120,220,160,.45),transparent 45%),
  radial-gradient(circle at 72% 35%,rgba(248,160,160,.45),transparent 45%),
  radial-gradient(circle at 50% 80%,rgba(120,210,240,.45),transparent 45%);filter:blur(40px)}
.headline{left:0;width:1366px;top:172px;text-align:center;font-size:36px;font-weight:700;color:var(--blue-text)}
.login-card{left:452px;top:256px;width:462px;height:378px;background:var(--white);border-radius:8px}
.field{left:65px;width:332px;height:48px;border:1px solid var(--blue-soft);border-radius:6px;display:flex;align-items:center;padding:0 14px;gap:14px;font-size:14px;color:var(--placeholder)}
.field .link{margin-left:auto;color:var(--green-text);font-weight:500}
.btn{display:flex;align-items:center;justify-content:center;border-radius:6px;font-size:14px;font-weight:600}
.btn--login{left:65px;top:194px;width:332px;height:48px;background:var(--blue);color:var(--white);box-shadow:0 10px 18px rgba(47,138,240,.3)}
.or{left:0;width:462px;top:264px;text-align:center;font-size:13px;color:var(--placeholder)}
.btn--alt{left:65px;top:296px;width:332px;height:48px;border:1px solid var(--red-soft);color:var(--red-soft);background:var(--white)}
.btn--signup{background:var(--green);color:var(--white);font-weight:500}
.note{font-size:14px;font-weight:500}
.note .link{color:var(--green);font-weight:600;margin-left:22px}
/* vault */
.search{left:285px;top:35px;width:736px;height:48px;background:var(--white);border-radius:8px;padding-left:36px;display:flex;align-items:center;font-size:14px;color:#9aa3ad}
.btn--add{left:1052px;top:35px;width:129px;height:50px;background:var(--green-bright);color:var(--white);font-size:22px;font-weight:500;gap:20px}
.nav-item{left:23px;width:231px;height:49px;border-radius:6px;display:flex;align-items:center;padding-left:20px;gap:26px;font-size:15px;font-weight:500}
.nav-item--active{background:var(--blue);color:var(--white);font-weight:700}
.tab{left:285px;width:133px;height:32px;border-radius:6px 6px 0 0;color:var(--white);font-size:14px;font-weight:700;display:flex;align-items:center;justify-content:space-between;padding:0 12px 0 16px}
.panel{background:var(--white);border-radius:0 8px 8px 8px}
.cat{top:16px;height:78px;border-radius:8px;padding:14px 12px;font-size:14px;font-weight:500}
.cat-title{display:flex;align-items:center;gap:12px;margin-left:2px}
.cat-sub{font-size:12px;margin-top:14px;opacity:.8}
.row{left:285px;width:736px;height:45px;background:var(--white);border-radius:6px;font-size:14px}
.row .check{position:absolute;left:19px;top:15px;width:14px;height:14px;border:1.5px solid var(--yellow);border-radius:2px}
.row .ico{position:absolute;left:66px;top:13px}
.row .name{position:absolute;left:108px;top:13px}
.row .date{position:absolute;left:538px;top:13px}
.row .more{position:absolute;left:705px;top:13px}
.folder{width:208px;height:48px;background:var(--cyan-pale);border-radius:6px;display:flex;align-items:center;padding:0 14px;gap:20px;font-size:14px}
.folder .more{margin-left:auto}
.folder--active{background:var(--cyan);color:var(--white);font-weight:700}
.detail-label{left:24px;font-size:10px;font-weight:600}
.detail-value{left:24px;font-size:14px;color:var(--muted)}
</style>
</head>
<body>
<div class="board">

  <section class="screen screen--login">
    <div class="abs brand" style="left:62px;top:40px;font-size:24px">
      <span class="brand-mark"></span><span>Lumen Keyvault</span>
    </div>
    <div class="abs note" style="left:1005px;top:51px;font-weight:500">Don't have an account?</div>
    <div class="abs btn btn--signup" style="left:1190px;top:39px;width:109px;height:41px;border-radius:8px">Sign up</div>

    <div class="abs glow"></div>
    <h1 class="abs headline">Welcome Back</h1>

    <form class="abs login-card">
      <div class="abs field" style="top:64px">
        <svg width="18" height="14" viewBox="0 0 18 14" fill="none" stroke="#5aa7ef" stroke-width="1.4"><rect x="1" y="1" width="16" height="12" rx="1.5"/><path d="M1 2l8 6 8-6"/></svg>
        <span>Enter your email</span>
      </div>
      <div class="abs field" style="top:129px">
        <svg width="16" height="18" viewBox="0 0 16 18" fill="none" stroke="#5aa7ef" stroke-width="1.4"><rect x="1.5" y="7.5" width="13" height="9.5" rx="1.5"/><path d="M4.5 7.5V5a3.5 3.5 0 017 0v2.5"/><circle cx="8" cy="12" r="1"/></svg>
        <span>Enter password</span>
        <span class="link">Forgot Password?</span>
      </div>
      <div class="abs btn btn--login">Login</div>
      <div class="abs or">OR</div>
      <div class="abs btn btn--alt">Continue with Nimbus</div>
    </form>

    <div class="abs note" style="left:571px;top:671px">Don't have an account?<span class="link">Sign up</span></div>
  </section>

  <section class="screen screen--vault">
    <div class="abs brand" style="left:23px;top:42px;font-size:26px;gap:14px">
      <span class="brand-mark" style="width:44px;height:44px"></span><span>Lumen Keyvault</span>
    </div>

    <nav>
      <div class="abs nav-item nav-item--active" style="top:121px">
        <svg width="18" height="18" viewBox="0 0 18 18" fill="#fff"><path d="M9 1l8 7v9h-5v-6H6v6H1V8z"/></svg>Vault
      </div>
      <div class="abs nav-item" style="top:184px">
        <svg width="22" height="16" viewBox="0 0 22 16" fill="#8cc0f2"><circle cx="7" cy="4" r="3.5"/><circle cx="15" cy="4" r="3"/><path d="M0 15c0-4 3-6 7-6s7 2 7 6z"/><path d="M13 9.5c4 0 9 1 9 5.5h-6c0-2-1-4-3-5.5z"/></svg>Shared with me
      </div>
      <div class="abs nav-item" style="top:241px">
        <svg width="18" height="20" viewBox="0 0 18 20" fill="none" stroke="#8cc0f2" stroke-width="1.8"><path d="M1 4h16M6 4V1h6v3M3 4l1 15h10l1-15M7 8v8M11 8v8"/></svg>Trash
      </div>
    </nav>

    <svg class="abs" style="left:41px;top:712px" width="22" height="22" viewBox="0 0 24 24" fill="#2f8af0"><path d="M12 8a4 4 0 100 8 4 4 0 000-8zm9.4 5.5l2 1.6-2 3.5-2.4-.9a8 8 0 01-2.4 1.4L16.2 22h-4l-.4-2.6a8 8 0 01-2.4-1.4l-2.4.9-2-3.5 2-1.6a8 8 0 010-2.8l-2-1.6 2-3.5 2.4.9a8 8 0 012.4-1.4L12.2 2h4l.4 2.6a8 8 0 012.4 1.4l2.4-.9 2 3.5-2 1.6a8 8 0 010 2.8z" transform="translate(-2 0)"/></svg>
    <div class="abs" role="img" aria-label="Profile photo of the account owner" style="left:88px;top:702px;width:42px;height:42px;border-radius:50%;background:linear-gradient(135deg,#2ec4ee,#8a4a3a)"></div>
    <div class="abs" style="left:150px;top:713px;font-size:14px;color:var(--blue-text);font-weight:500">My Account</div>

    <div class="abs search">Search</div>
    <div class="abs btn btn--add">
      <svg width="26" height="26" viewBox="0 0 26 26" fill="none" stroke="#fff" stroke-width="2"><rect x="2" y="5" width="17" height="19" rx="2"/><path d="M6 11h9M6 15h9M6 19h6M21 1v8M17 5h8"/></svg>Add
    </div>
    <svg class="abs" style="left:1241px;top:51px" width="20" height="20" viewBox="0 0 20 20" fill="#1dbf63"><path d="M10 1a6 6 0 016 6v5l2 3H2l2-3V7a6 6 0 016-6zM7.5 17h5a2.5 2.5 0 01-5 0z"/></svg>
    <svg class="abs" style="left:1292px;top:52px" width="16" height="20" viewBox="0 0 16 20" fill="#5ed28c"><path d="M1 1h14v18l-7-5-7 5z"/></svg>

    <!-- Category -->
    <div class="abs tab" style="top:103px;background:var(--red)"><span>Category</span><span>⋮</span></div>
    <div class="abs panel" style="left:285px;top:135px;width:736px;height:130px">
      <div class="abs cat" style="left:20px;width:114px;background:var(--red);color:#fff">
        <div class="cat-title" style="font-weight:700"><svg width="20" height="16" viewBox="0 0 20 16" fill="#fff"><path d="M0 1h7l2 2h11v13H0z"/></svg>General</div>
        <div class="cat-sub" style="opacity:.9">Manage Access</div>
      </div>
      <div class="abs cat" style="left:149px;width:113px;background:#d6f3fb;color:#43c2e8">
        <div class="cat-title"><svg width="20" height="17" viewBox="0 0 20 17" fill="#43c2e8"><path d="M7 0h6v3h7v14H0V3h7zM9 1.5v1.5h2V1.5z"/></svg>Work</div>
        <div class="cat-sub">Manage Access</div>
      </div>
      <div class="abs cat" style="left:277px;width:164px;background:#d3f7df;color:#22b45a">
        <div class="cat-title"><svg width="20" height="16" viewBox="0 0 20 16" fill="#22b45a"><path d="M0 1h7l2 2h11v13H0z"/><circle cx="10" cy="8" r="2" fill="#d3f7df"/><path d="M6.5 13c0-2 1.5-3 3.5-3s3.5 1 3.5 3z" fill="#d3f7df"/></svg>Shared with me</div>
        <div class="cat-sub">Manage Access</div>
      </div>
      <div class="abs cat" style="left:455px;width:113px;background:#dfe6fb;color:#4a7de0">
        <div class="cat-title"><svg width="22" height="18" viewBox="0 0 22 18" fill="none" stroke="#4a7de0" stroke-width="1.8"><rect x="1" y="4" width="20" height="13" rx="2"/><path d="M7 4V1h8v3M1 10h20"/></svg>Travel</div>
        <div class="cat-sub">Manage Access</div>
      </div>
      <div class="abs cat" style="left:583px;width:113px;background:#fde7d6;color:#f59a4b">
        <div class="cat-title"><svg width="20" height="16" viewBox="0 0 20 16" fill="#f59a4b"><rect width="20" height="16" rx="2"/><path d="M2 3l8 6 8-6" stroke="#fde7d6" stroke-width="1.6" fill="none"/></svg>Mail</div>
        <div class="cat-sub">Manage Access</div>
      </div>
      <svg class="abs" style="left:362px;top:112px" width="12" height="8" viewBox="0 0 12 8" fill="none" stroke="#555" stroke-width="1.6"><path d="M1 1l5 5 5-5"/></svg>
    </div>

    <!-- Last used -->
    <div class="abs tab" style="top:277px;background:var(--yellow)"><span>Last Used</span><span>⋮</span></div>
    <div class="abs" style="left:823px;top:280px;font-size:14px;font-weight:500">Last Modified</div>

    <div class="abs row" style="top:308px;box-shadow:0 4px 10px rgba(248,201,58,.25)">
      <span class="check" style="background:var(--yellow);box-shadow:inset 0 0 0 2px #fff"></span>
      <svg class="ico" width="20" height="16" viewBox="0 0 20 16" fill="none" stroke="#f8c93a" stroke-width="1.6"><path d="M1 1h6l2 2h10v12H1z"/></svg>
      <span class="name" style="font-weight:700">Social Media</span><span class="date">03 June 2023</span><span class="more" style="font-weight:700">⋮</span>
    </div>
    <div class="abs row" style="top:366px">
      <span class="check"></span>
      <svg class="ico" width="20" height="16" viewBox="0 0 20 16" fill="none" stroke="#f8c93a" stroke-width="1.6"><path d="M1 1h6l2 2h10v12H1z"/></svg>
      <span class="name">Work</span><span class="date">03 June 2023</span><span class="more" style="font-weight:700">⋮</span>
    </div>
    <div class="abs row" style="top:424px">
      <span class="check"></span>
      <svg class="ico" width="20" height="16" viewBox="0 0 20 16" fill="none" stroke="#f8c93a" stroke-width="1.6"><path d="M1 1h6l2 2h10v12H1z"/></svg>
      <span class="name">Banking</span><span class="date">03 June 2023</span><span class="more" style="font-weight:700">⋮</span>
    </div>
    <div class="abs row" style="top:482px">
      <span class="check"></span>
      <svg class="ico" width="20" height="16" viewBox="0 0 20 16" fill="none" stroke="#f8c93a" stroke-width="1.6"><path d="M1 1h6l2 2h10v12H1z"/></svg>
      <span class="name">Authentication</span><span class="date">03 June 2023</span><span class="more" style="font-weight:700">⋮</span>
    </div>

    <!-- Folders -->
    <div class="abs tab" style="top:555px;background:var(--cyan)"><span>Folders</span><span>⋮</span></div>
    <div class="abs panel" style="left:285px;top:587px;width:736px;height:200px">
      <div class="abs folder" style="left:25px;top:25px"><svg width="20" height="16" viewBox="0 0 20 16" fill="none" stroke="#2ec4ee" stroke-width="1.6"><path d="M1 1h6l2 2h10v12H1z"/></svg>Social Media<span class="more" style="color:var(--cyan)">⋮</span></div>
      <div class="abs folder" style="left:263px;top:25px"><svg width="20" height="16" viewBox="0 0 20 16" fill="none" stroke="#2ec4ee" stroke-width="1.6"><path d="M1 1h6l2 2h10v12H1z"/></svg>Social Media<span class="more" style="color:var(--cyan)">⋮</span></div>
      <div class="abs folder" style="left:501px;top:25px"><svg width="20" height="16" viewBox="0 0 20 16" fill="none" stroke="#2ec4ee" stroke-width="1.6"><path d="M1 1h6l2 2h10v12H1z"/></svg>Social Media<span class="more" style="color:var(--cyan)">⋮</span></div>
      <div class="abs folder folder--active" style="left:25px;top:89px"><svg width="20" height="16" viewBox="0 0 20 16" fill="none" stroke="#fff" stroke-width="1.6"><path d="M1 1h6l2 2h10v12H1z"/></svg>Chirper<span class="more">⋮</span></div>
      <div class="abs folder" style="left:263px;top:89px"><svg width="20" height="16" viewBox="0 0 20 16" fill="none" stroke="#2ec4ee" stroke-width="1.6"><path d="M1 1h6l2 2h10v12H1z"/></svg>Chirper<span class="more" style="color:var(--cyan)">⋮</span></div>
      <div class="abs folder" style="left:501px;top:89px"><svg width="20" height="16" viewBox="0 0 20 16" fill="none" stroke="#2ec4ee" stroke-width="1.6"><path d="M1 1h6l2 2h10v12H1z"/></svg>Chirper<span class="more" style="color:var(--cyan)">⋮</span></div>
      <div class="abs folder" style="left:25px;top:153px"><svg width="20" height="16" viewBox="0 0 20 16" fill="none" stroke="#2ec4ee" stroke-width="1.6"><path d="M1 1h6l2 2h10v12H1z"/></svg>Work<span class="more" style="color:var(--cyan)">⋮</span></div>
      <div class="abs folder" style="left:263px;top:153px"><svg width="20" height="16" viewBox="0 0 20 16" fill="none" stroke="#2ec4ee" stroke-width="1.6"><path d="M1 1h6l2 2h10v12H1z"/></svg>Work<span class="more" style="color:var(--cyan)">⋮</span></div>
      <div class="abs folder" style="left:501px;top:153px"><svg width="20" height="16" viewBox="0 0 20 16" fill="none" stroke="#2ec4ee" stroke-width="1.6"><path d="M1 1h6l2 2h10v12H1z"/></svg>Work<span class="more" style="color:var(--cyan)">⋮</span></div>
    </div>

    <!-- Details -->
    <div class="abs" style="left:1053px;top:124px;width:276px;height:38px;background:var(--white);border-bottom:1px solid var(--line);display:flex;font-size:14px;font-weight:500">
      <div style="width:138px;background:var(--blue);color:#fff;border-radius:6px 6px 0 0;display:flex;align-items:center;padding-left:23px">Details</div>
      <div style="width:138px;color:var(--blue-text);display:flex;align-items:center;padding-left:21px">Activity</div>
    </div>
    <aside class="abs" style="left:1053px;top:162px;width:276px;height:577px;background:var(--white);border-radius:0 0 8px 8px">
      <div class="abs" style="left:24px;top:20px;font-size:14px;font-weight:700">Social Media</div>
      <svg class="abs" style="left:68px;top:60px" width="128" height="104" viewBox="0 0 128 104" fill="#dde8fb"><path d="M4 0h40l10 12h70a4 4 0 014 4v84a4 4 0 01-4 4H4a4 4 0 01-4-4V4a4 4 0 014-4z"/></svg>
      <div class="abs detail-label" style="top:222px">Category</div><div class="abs detail-value" style="top:240px">Social Media</div>
      <div class="abs detail-label" style="top:277px">Owner</div><div class="abs detail-value" style="top:295px">My Account</div>
      <div class="abs detail-label" style="top:332px">Last Modified</div><div class="abs detail-value" style="top:350px">03 June 2023</div>
      <div class="abs detail-label" style="top:387px">Last Opened</div><div class="abs detail-value" style="top:405px">Today 04:25 pm</div>
      <div class="abs detail-label" style="top:442px">Created</div><div class="abs detail-value" style="top:460px">02 June 2023</div>
      <div class="abs detail-label" style="top:497px">Note</div>
      <div class="abs btn" style="left:20px;top:515px;width:82px;height:36px;background:var(--blue-pale);color:var(--blue-text);font-weight:500;gap:16px">
        <svg width="16" height="20" viewBox="0 0 16 20" fill="#2f8af0"><path d="M0 2a2 2 0 012-2h8l6 6v12a2 2 0 01-2 2H2a2 2 0 01-2-2z"/><path d="M8 8v8M4 12h8" stroke="#fff" stroke-width="1.8"/></svg>Add
      </div>
    </aside>
  </section>

</div>
</body>
</html>
```